Web Design Project

The aim of this project to design a website for a service that would offer services for small business and non profit organizations using opensource software that is weaved to work together in harmony.

The website name is: velisto.net

Velisto in Arabic means: cabbage. Cabbage is composed of leaves, actually there is nothing except leaves. Each leave by itself is not called cabbage, but a collection of leaves that are organized in a central way would give us cabbage.

Same idea for Velisto where open source software very well organized and integrated would create a new thing with a new value.
Updates

Target Market(s)

Small business, Europe, Africa, Far east and Middle east

Industry/Entity Type

Small Business

Requirements
Must have
• The website would offer the following sections:
* Home page
* Benefits: value of velisto
* Applications: applications offered by velisto
* Pricing
* Purchase
* Customer log in
* Support
- FAQ
- Knowledge base
- Forums
- Open tickets

Please take the following consideration in design:
* White should predominate
* Only black and the colors of logo are permitted (attched)
Nice to have
• Design is better to express:
* Openness
* Dynamic
* Usable
* Cost effective

Files

```html
<!DOCTYPE html>
<html lang="en">
<head>
<meta charset="utf-8">
<title>Velisto — Solutions for Small Business and NPOs</title>
<link href="https://fonts.googleapis.com/css2?family=Raleway:wght@300;400;600;700&family=Arimo:wght@400;700&display=swap" rel="stylesheet">
<style>
:root{
  --pink:#a8377c;
  --blue:#1b9ad8;
  --green:#8cc63f;
  --ink:#1c1c1c;
  --text:#555;
  --muted:#777;
  --line:#e2e2e2;
  --footer:#262626;
  --footer-deep:#1a1a1a;
  --footer-text:#c9c9c9;
}
*{box-sizing:border-box;margin:0;padding:0}
html,body{width:742px;height:1200px;overflow:hidden;background:#fff}
body{font-family:Arimo,Arial,sans-serif;color:var(--text);position:relative}
.abs{position:absolute}
a{color:inherit;text-decoration:none}

/* header */
.brand{left:91px;top:14px;width:110px;height:48px}
.brand-dot{position:absolute;left:18px;top:0;width:22px;height:22px;border-radius:50%;background:var(--green)}
.brand-name{position:absolute;left:0;top:26px;font-family:Raleway,sans-serif;font-weight:600;font-size:22px;color:var(--ink);letter-spacing:.3px}
.contact-bar{right:96px;top:15px;font-size:8px;color:#555;display:flex;gap:14px;align-items:center;font-weight:700}
.contact-bar span{display:flex;align-items:center;gap:4px}

/* nav */
.nav{left:0;top:74px;width:742px;height:27px;border-top:1px solid var(--line);border-bottom:1px solid var(--line)}
.nav ul{list-style:none;display:flex;position:absolute;left:91px;top:-1px;height:27px}
.nav li{font-family:Raleway,sans-serif;font-weight:700;font-size:8px;color:#222;border-left:1px solid var(--line);height:27px;display:flex;align-items:center;justify-content:center}
.nav li:last-child{border-right:1px solid var(--line)}
.nav li.current{color:var(--blue);border-top:2px solid var(--blue)}

/* hero */
.hero{left:0;top:103px;width:742px;height:259px;background:linear-gradient(90deg,#f4f5f7 0%,#eef0f3 45%,#e3e7ec 100%);overflow:hidden}
.hero-photo{position:absolute;left:430px;top:0;width:312px;height:259px;background:radial-gradient(ellipse at 45% 55%,#e9d2c2 0%,#d9c3bd 35%,#dfe3e8 75%)}
.hero-title{left:124px;top:144px;font-size:21px;font-weight:400;color:var(--pink)}
.hero-sub{left:124px;top:183px;font-size:13px;color:#111}
.hero-text{left:124px;top:206px;width:284px;font-size:8.4px;line-height:12.5px;font-weight:700;color:#555}
.btn-pink{left:124px;top:289px;width:59px;height:19px;background:var(--pink);border-radius:3px;color:#fff;font-size:8px;display:flex;align-items:center;justify-content:center;box-shadow:0 2px 0 #6f1f50}
.hero-arrow{top:221px;width:23px;height:23px;border-radius:50%;background:#3a3a3a}
.dots{left:355px;top:342px;display:flex;gap:6px}
.dots i{width:8px;height:8px;border-radius:50%;background:#bbb;border:1px solid #999}
.dots i:first-child{background:#666}
.hero-rule{left:0;top:362px;width:742px;height:4px;background:#e4e4e4}

/* features */
.feature{top:390px;width:224px;height:146px;text-align:center}
.feature h3{font-family:Raleway,sans-serif;font-weight:700;font-size:10px;color:var(--pink);margin-top:73px}
.feature p{font-size:8.6px;line-height:11px;color:var(--muted);margin:5px auto 0;width:150px}
.feature .more{display:block;margin-top:12px;font-size:8.6px;color:var(--blue)}
.feature .icon{position:absolute;left:97px;top:22px}
.feature.highlight{background:var(--blue);border-radius:3px}
.feature.highlight h3,.feature.highlight p{color:#fff}
.feature.highlight .pill{display:inline-block;margin-top:8px;background:#fff;color:var(--blue);font-size:8.4px;padding:2px 8px;border-radius:8px}

/* process */
.section-title{left:0;top:570px;width:742px;text-align:center;font-family:Raleway,sans-serif;font-weight:300;font-size:25px;color:#111}
.step{top:619px;width:112px;text-align:center}
.step .ring{width:50px;height:50px;border-radius:50%;border:2px solid var(--blue);margin:0 auto;background:#fff;display:flex;align-items:center;justify-content:center}
.step h4{font-family:Raleway,sans-serif;font-weight:700;font-size:10px;color:var(--pink);margin-top:17px}
.step p{font-size:7.6px;line-height:11.5px;color:var(--muted);margin:6px auto 0;width:90px}
.cta{left:0;top:813px;width:742px;text-align:center;font-family:Raleway,sans-serif;font-size:17px;color:#444}
.cta b{color:var(--blue);font-weight:700}
.to-top{width:18px;height:18px;background:#a9b3ba;border-radius:2px}

/* clients */
.clients-label{left:91px;top:886px;font-family:Raleway,sans-serif;font-weight:700;font-size:7.4px;color:#333}
.clients-rule{left:91px;top:898px;width:557px;height:1px;background:var(--line)}
.clients-nav{left:623px;top:882px;display:flex;gap:1px}
.clients-nav i{width:12px;height:12px;background:#ddd}
.clients-nav i+i{background:#bbb}
.clients{left:91px;top:916px;width:557px;height:54px;display:flex}
.client{flex:1;display:flex;align-items:center;justify-content:center;gap:6px;border-right:1px solid #eee;font-family:Raleway,sans-serif;font-weight:700;font-size:18px;color:#333}
.client:last-child{border-right:0}
.client i{width:12px;height:12px;border-radius:50%;background:#333}

/* footer */
.footer-top{left:0;top:1010px;width:742px;height:3px;background:var(--green)}
.footer{left:0;top:1013px;width:742px;height:187px;background:var(--footer)}
.fcol{top:1033px;width:125px;font-size:7.5px;line-height:12px;color:var(--footer-text)}
.fcol h5{font-family:Raleway,sans-serif;font-weight:700;font-size:8px;color:#fff;padding-bottom:6px;border-bottom:1px solid #3a3a3a;margin-bottom:10px}
.addr{width:130px}
.addr div{margin-bottom:6px;padding-left:14px;position:relative;white-space:nowrap}
.addr svg{position:absolute;left:0;top:1px}
.addr b{color:#ddd}
.tweet{background:#333;padding:8px 6px;height:84px}
.tweet .head{text-align:right;color:#ddd;margin-bottom:2px}
.tweet p{color:var(--blue)}
.links div{margin-bottom:5px}
.footer-base{left:84px;top:1174px;width:571px;height:26px;background:var(--footer-deep);font-size:7px;color:#aaa;padding:9px 12px}
</style>
</head>
<body>

<header>
  <div class="abs brand"><span class="brand-dot"></span><span class="brand-name">velisto</span></div>
  <div class="abs contact-bar">
    <span><svg width="9" height="9" viewBox="0 0 10 10"><path d="M2 1l2 2-1 1.5c.6 1.3 1.3 2 2.5 2.5L7 6l2 2-1.5 1.5C4 9 1 6 .5 2.5z" fill="#666"/></svg>Call Us Today! 1.480.372.615</span>
    <span><svg width="10" height="8" viewBox="0 0 10 8"><rect width="10" height="8" fill="#777"/><path d="M0 0l5 4 5-4" stroke="#fff" fill="none"/></svg>info@velistomail.net</span>
  </div>
  <nav class="abs nav">
    <ul>
      <li class="current" style="width:45px">HOME</li>
      <li style="width:60px">BENEFITS</li>
      <li style="width:79px">APPLICATIONS</li>
      <li style="width:53px">PRICING</li>
      <li style="width:67px">PURCHASE</li>
      <li style="width:92px">CUSTOMER LOG IN</li>
      <li style="width:60px">SUPPORT</li>
      <li style="width:59px">CONTACT</li>
    </ul>
  </nav>
</header>

<section class="abs hero">
  <div class="hero-photo" role="img" aria-label="Photo of a smiling woman pointing upward"></div>
</section>
<h1 class="abs hero-title">Solutions for Small Business and NPOs</h1>
<p class="abs hero-sub">Velisto makes it as simple as 1.2.3.</p>
<p class="abs hero-text">Lorem Ipsum is simply dummy text of the printing and typesetting industry. Lorem Ipsum has been the industry's standard dummy text ever since the 1500s, when an unknown printer took a galley of type and scrambled it to make a type specimen book. It has survived not only five centuries, but also the leap into electronic typesetting, remaining essentially unchanged.</p>
<a class="abs btn-pink">Blue Button</a>
<div class="abs hero-arrow" style="left:5px"><svg width="23" height="23"><path d="M13 7l-5 4.5 5 4.5" stroke="#fff" stroke-width="2" fill="none"/></svg></div>
<div class="abs hero-arrow" style="left:714px"><svg width="23" height="23"><path d="M10 7l5 4.5-5 4.5" stroke="#fff" stroke-width="2" fill="none"/></svg></div>
<div class="abs dots"><i></i><i></i><i></i></div>
<div class="abs hero-rule"></div>

<section>
  <div class="abs feature" style="left:62px">
    <svg class="icon" width="30" height="30" viewBox="0 0 30 30"><circle cx="15" cy="15" r="12" fill="none" stroke="var(--pink)" stroke-width="2"/><text x="15" y="20" text-anchor="middle" font-family="Arimo" font-weight="700" font-size="14" fill="var(--blue)">?</text></svg>
    <h3>Why Velisto?</h3>
    <p>Lorem ipsum dolor sit amet, consectetur adipisicing elit mobile devices.</p>
    <a class="more">Learn More ›</a>
  </div>
  <div class="abs feature highlight" style="left:258px">
    <svg class="icon" width="48" height="48" viewBox="0 0 48 48" style="left:88px;top:12px"><circle cx="24" cy="24" r="23" fill="#fff"/><path d="M13 17h4l3 12h12l3-9H19" fill="none" stroke="#333" stroke-width="2"/><circle cx="22" cy="33" r="2" fill="#333"/><circle cx="30" cy="33" r="2" fill="#333"/></svg>
    <h3 style="margin-top:69px">Buy Now</h3>
    <p style="width:180px">Lorem ipsum dolor sit amet, consectetur adipisicing elit mobile devices.</p>
    <span class="pill">Learn More</span>
  </div>
  <div class="abs feature" style="left:452px">
    <svg class="icon" width="30" height="30" viewBox="0 0 30 30"><rect x="8" y="3" width="16" height="22" fill="none" stroke="var(--blue)" stroke-width="2"/><path d="M12 10h8M12 14h8M12 18h5" stroke="var(--blue)" stroke-width="1.5"/><path d="M2 8h4M1 12h5M3 16h3" stroke="#d33" stroke-width="1.5"/></svg>
    <h3>User Guide</h3>
    <p>Lorem ipsum dolor sit amet, consectetur adipisicing elit mobile devices.</p>
    <a class="more">Learn More ›</a>
  </div>
</section>

<h2 class="abs section-title">How we do?</h2>
<svg class="abs" style="left:0;top:600px" width="742" height="215" viewBox="0 0 742 215">
  <line x1="91" y1="44" x2="648" y2="44" stroke="#ccc" stroke-dasharray="3 3"/>
  <g fill="#ccc"><path d="M110 41l5 3-5 3z"/><path d="M222 41l5 3-5 3z"/><path d="M335 41l5 3-5 3z"/><path d="M446 41l5 3-5 3z"/><path d="M558 41l5 3-5 3z"/></g>
  <path d="M91 170q0 12 12 12h252l15 22 15-22h252q12 0 12-12" fill="none" stroke="#ddd"/>
</svg>
<div class="abs step" style="left:89px">
  <div class="ring"><svg width="24" height="24" viewBox="0 0 24 24"><rect x="4" y="5" width="12" height="14" fill="#d33"/><rect x="8" y="8" width="12" height="12" fill="none" stroke="var(--blue)" stroke-width="2"/></svg></div>
  <h4>Understand</h4><p>Scenester cred you probably haven't heard of them, vinyl craft beer blog stumptown</p>
</div>
<div class="abs step" style="left:201px">
  <div class="ring"><svg width="24" height="24" viewBox="0 0 24 24"><circle cx="12" cy="10" r="6" fill="#f5a623"/><rect x="9" y="16" width="6" height="4" fill="#555"/><path d="M12 1v2M3 10h2M19 10h2M5 4l1.5 1.5M19 4l-1.5 1.5" stroke="#d33" stroke-width="1.5"/></svg></div>
  <h4>Think</h4><p>Scenester cred you probably haven't heard of them, vinyl craft beer blog stumptown</p>
</div>
<div class="abs step" style="left:314px">
  <div class="ring"><svg width="24" height="24" viewBox="0 0 24 24"><circle cx="9" cy="13" r="5" fill="none" stroke="#d33" stroke-width="3" stroke-dasharray="2 1.5"/><circle cx="17" cy="8" r="4" fill="none" stroke="#d33" stroke-width="2.5" stroke-dasharray="2 1.5"/></svg></div>
  <h4>Develop</h4><p>Scenester cred you probably haven't heard of them, vinyl craft beer blog stumptown</p>
</div>
<div class="abs step" style="left:425px">
  <div class="ring"><svg width="24" height="24" viewBox="0 0 24 24"><path d="M4 20L17 7" stroke="#d33" stroke-width="3"/><path d="M19 2v4M17 4h4M12 3v2M11 4h2" stroke="var(--blue)" stroke-width="1.3"/></svg></div>
  <h4>Customize</h4><p>Scenester cred you probably haven't heard of them, vinyl craft beer blog stumptown</p>
</div>
<div class="abs step" style="left:537px">
  <div class="ring"><svg width="24" height="24" viewBox="0 0 24 24"><circle cx="12" cy="9" r="7" fill="var(--green)"/><rect x="11" y="14" width="2" height="8" fill="#7a4a2a"/><path d="M8 22h8" stroke="#7a4a2a" stroke-width="1.5"/></svg></div>
  <h4>Implement</h4><p>Scenester cred you probably haven't heard of them, vinyl craft beer blog stumptown</p>
</div>
<p class="abs cta">Do you like our Services? <b>Contact Now ›</b></p>
<div class="abs to-top" style="left:713px;top:799px"><svg width="18" height="18"><path d="M5 11l4-4 4 4" stroke="#fff" stroke-width="1.5" fill="none"/></svg></div>

<section>
  <h6 class="abs clients-label">OUR CLIENTS</h6>
  <div class="abs clients-rule"></div>
  <div class="abs clients-nav"><i></i><i></i></div>
  <div class="abs clients">
    <div class="client"><i></i>lumora</div>
    <div class="client">brisko</div>
    <div class="client">fennwick</div>
    <div class="client">corvana</div>
    <div class="client">tallis</div>
  </div>
</section>

<footer>
  <div class="abs footer-top"></div>
  <div class="abs footer"></div>
  <div class="abs fcol addr" style="left:91px">
    <h5>ADDRESS:</h5>
    <div><svg width="8" height="10" viewBox="0 0 8 10"><path d="M4 10L1 5a3 3 0 116 0z" fill="#888"/></svg><b>Address:</b><br>No.14 - 52817 Harbor Lane</div>
    <div><svg width="9" height="9" viewBox="0 0 10 10"><path d="M2 1l2 2-1 1.5c.6 1.3 1.3 2 2.5 2.5L7 6l2 2-1.5 1.5C4 9 1 6 .5 2.5z" fill="#888"/></svg><b>Phone:</b><br>+ 1 (415) 902 3376</div>
    <div><svg width="10" height="8" viewBox="0 0 10 8"><rect width="10" height="8" fill="#888"/><path d="M0 0l5 4 5-4" stroke="#262626" fill="none"/></svg><b>Email:</b><br>support@velisto.net</div>
  </div>
  <div class="abs fcol" style="left:234px;width:128px">
    <h5>STAY CONNECT</h5>
    <div class="tweet"><div class="head">Latest tweet</div><p>@Lorem ipsum dolor sit amet, consectetur adipiscing elit. Nulla at felis mi, at auctor mi. Donec vel nibh sem. Etiam ut lacus a dui accumsan accumsan.</p></div>
  </div>
  <div class="abs fcol" style="left:376px;width:128px">
    <h5>DISCLAIMER</h5>
    <p>Important: Lorem ipsum dolor sit amet, consectetur adipiscing elit. Nulla at felis mi, at auctor mi. Donec vel nibh sem. Etiam ut lacus a dui accumsan accumsan.</p>
  </div>
  <div class="abs fcol links" style="left:520px">
    <h5>QUICK LINKS</h5>
    <div>Home</div><div>Our Benefits</div><div>Our Applications</div><div>Contact Us</div>
  </div>
  <div class="abs footer-base">Copyright 2013 Velisto.net All rights reserved.</div>
  <div class="abs to-top" style="left:713px;top:1156px"><svg width="18" height="18"><path d="M5 11l4-4 4 4" stroke="#fff" stroke-width="1.5" fill="none"/></svg></div>
</footer>

</body>
</html>
```